Fully Functional Wix Website, Not Just Images

Please read all instructions carefully. This is NOT merely a design project where the artist will deliver static images. This project requires that the designer build a fully functional SEO optimized website within Wix then transfer full ownership to me. See attached "instructions for design" file. I have wix for other websites. Only wix is acceptable. Do not submit more than 1 design per designer. If you submit more than 1 design I will award to someone else.

Target Market(s)

see attachments and trelvanox482.com

Industry/Entity Type

Coding

Coded - Design and coding required

Number of Pages Required

4 page

Font styles to use
Other font styles liked:
• see attachments and trelvanox482.com

Requirements
Must have
Nice to have
Should not have

```html
<!DOCTYPE html>
<html lang="en">
<head>
<meta charset="utf-8">
<title>Captain Harlow's Boat Training & Charters</title>
<link href="https://fonts.googleapis.com/css2?family=Lexend+Exa:wght@500;600&family=Roboto:ital,wght@0,400;0,500;0,700;1,400;1,500&display=swap" rel="stylesheet">
<style>
:root{
  --navy:#1b2450;
  --navy-deep:#141b3d;
  --gold:#e2a92b;
  --gold-soft:#f0c766;
  --ink:#1d2233;
  --muted:#5d6372;
  --white:#ffffff;
  --mist:#eef1f6;
}
*{margin:0;padding:0;box-sizing:border-box}
html,body{width:1200px;height:3369px;overflow:hidden}
body{font-family:"Roboto",sans-serif;color:var(--ink);background:var(--white);position:relative}
.abs{position:absolute}
.display{font-family:"Lexend Exa",sans-serif;font-weight:600;letter-spacing:-1px}
.btn{position:absolute;display:flex;align-items:center;justify-content:center;gap:8px;font-weight:700;font-size:14px;border-radius:4px;text-transform:uppercase}
.btn-gold{background:var(--gold);color:var(--white)}
.btn-navy{background:var(--navy);color:var(--white)}
.eyebrow{position:absolute;left:0;width:1200px;text-align:center;font-weight:700;font-size:17px;color:var(--navy)}
.eyebrow::before,.eyebrow::after{content:"";display:inline-block;width:34px;height:3px;background:var(--gold);vertical-align:middle;margin:0 12px}
.section-title{position:absolute;left:0;width:1200px;text-align:center;font-size:40px}
.section-title .hl{color:var(--gold)}
.section-sub{position:absolute;left:0;width:1200px;text-align:center;font-size:17px;color:var(--muted)}

/* header */
.topbar{left:0;top:0;width:1200px;height:72px;background:var(--white)}
.brand-badge{left:100px;top:6px;width:130px;height:124px;border-radius:50%;background:var(--white);box-shadow:0 2px 8px rgba(0,0,0,.2);display:flex;align-items:center;justify-content:center;text-align:center;z-index:5}
.brand-badge span{width:96px;height:96px;border-radius:50%;background:var(--navy);color:var(--white);font-size:11px;font-weight:700;display:flex;align-items:center;justify-content:center;line-height:1.3;padding:8px}
.tagline{left:307px;top:24px;font-size:18px;font-weight:700;color:var(--gold);word-spacing:3px}
.motto{left:713px;top:28px;font-size:14px;font-weight:500;color:var(--ink)}
.navbar{left:0;top:72px;width:1200px;height:46px;background:var(--navy)}
.nav-link{position:absolute;top:87px;font-size:14px;font-weight:500;color:var(--white)}
.nav-link.active{color:var(--gold)}
.nav-active-bar{left:320px;top:114px;width:38px;height:3px;background:var(--gold)}

/* hero */
.hero-media{left:0;top:118px;width:1200px;height:556px;background:linear-gradient(180deg,#3a5378 0%,#7c7e86 30%,#d28a3e 48%,#5b4a44 58%,#23324d 100%)}
.hero-shade{left:0;top:118px;width:700px;height:556px;background:linear-gradient(90deg,rgba(10,20,40,.55),rgba(10,20,40,0))}
.hero-title{left:106px;top:238px;font-size:70px;line-height:80px;color:var(--white);letter-spacing:-2px}
.hero-kicker{left:111px;top:408px;font-size:22px;font-weight:700;color:var(--white)}
.hero-copy{left:111px;top:450px;width:540px;font-size:14px;font-weight:500;line-height:26px;color:var(--white)}
.hero-quote{left:1005px;top:348px;width:160px;font-size:13px;font-style:italic;font-weight:500;color:var(--white);line-height:19px}
.dot{position:absolute;top:611px;width:10px;height:10px;border-radius:50%;background:var(--white)}

/* books */
.books-bg{left:0;top:674px;width:1200px;height:797px;background:linear-gradient(180deg,#f6f7fa 0%,#e9edf3 60%,#dfe5ee 100%)}
.book{position:absolute;top:950px;height:322px;background:linear-gradient(180deg,#1d3f8a,#274f9e 55%,#16306a);box-shadow:0 8px 18px rgba(0,0,0,.3)}
.books-note{left:0;width:1200px;top:1398px;text-align:center;font-size:14px;color:var(--muted)}

/* captain */
.captain-photo{left:111px;top:1556px;width:261px;height:376px;background:linear-gradient(180deg,#c9ced6,#a7aeba);border-radius:2px}
.meet{left:395px;top:1574px;font-size:17px;font-weight:700;color:var(--navy)}
.meet::before,.meet::after{content:"";display:inline-block;width:32px;height:3px;background:var(--gold);vertical-align:middle;margin:0 10px}
.meet::before{margin-left:0}
.cap-head{left:395px;top:1604px;font-size:20px;line-height:29px;color:var(--navy);letter-spacing:-.5px}
.cap-head .hl{color:var(--gold)}
.cap-copy{left:396px;top:1668px;width:287px;font-size:12.5px;line-height:21.5px;color:var(--muted);text-align:justify}
.cred{position:absolute;left:768px;display:flex;align-items:center;gap:26px;font-size:14px;color:var(--muted);line-height:21px}
.cred i{flex:none;width:40px;height:40px;border-radius:50%;background:var(--navy);display:flex;align-items:center;justify-content:center}
.cred i.g{background:var(--gold)}
.cap-quote{left:770px;top:1864px;font-size:16px;font-style:italic;line-height:23px;color:var(--gold)}
.cap-quote span{color:var(--navy);padding-left:6px}

/* testimonials */
.reviews-bg{left:0;top:2024px;width:1200px;height:529px;background:linear-gradient(160deg,#1d2b5a 0%,#2b3e72 40%,#17234b 100%)}
.card{position:absolute;top:2252px;height:218px;background:var(--white);border-radius:4px;box-shadow:0 6px 16px rgba(0,0,0,.25)}
.rating-card{background:#f3f4f7}
.avatar{position:absolute;left:16px;top:18px;width:68px;height:68px;border-radius:50%;background:#c58b6a}
.rv-name{position:absolute;left:108px;top:34px;font-size:14px;font-weight:500}
.stars{position:absolute;font-size:15px;color:var(--gold);letter-spacing:1px}
.qmark{position:absolute;right:20px;top:26px;font-size:30px;font-weight:700;color:var(--navy);line-height:1}
.rv-text{position:absolute;left:22px;top:112px;width:205px;font-size:13.5px;line-height:20px;color:#555}
.arrow-c{position:absolute;top:2345px;width:30px;height:30px;border:2px solid var(--white);border-radius:50%;display:flex;align-items:center;justify-content:center}

/* services */
.svc{position:absolute;top:2788px;width:230px;text-align:center}
.svc .ic{width:68px;height:68px;border:3px solid var(--navy);border-radius:50%;margin:0 auto 20px;display:flex;align-items:center;justify-content:center}
.svc.feat .ic{border-color:var(--gold)}
.svc h3{font-size:21px;font-weight:500;color:var(--ink)}
.svc.feat h3{color:var(--gold);font-weight:700}
.svc p{font-size:13.5px;line-height:20px;color:var(--muted);margin-top:2px;height:60px}
.svc a{display:block;margin-top:12px;font-size:12px;font-weight:700;color:var(--navy);text-decoration:none}

/* footer */
.footer-motto{left:108px;top:3198px;font-size:27px;font-style:italic;font-weight:500;line-height:38px;color:var(--gold)}
.footer-badge{left:542px;top:3177px;width:116px;height:116px;border-radius:50%;background:var(--white);border:4px solid var(--gold);display:flex;align-items:center;justify-content:center;text-align:center;font-size:11px;font-weight:700;color:var(--navy);line-height:1.3;padding:14px}
.footer-line{left:723px;top:3244px;font-size:18px;font-weight:500;color:var(--white)}
.rule{left:111px;top:3316px;width:978px;height:1px;background:rgba(255,255,255,.55)}
.copy{left:113px;top:3338px;font-size:12px;color:var(--white)}
.social{position:absolute;top:3328px;width:22px;height:22px;border:2px solid var(--white);border-radius:50%}
</style>
</head>
<body>

<!-- Header -->
<div class="abs topbar"></div>
<div class="abs brand-badge"><span>Captain Harlow's Boat Training &amp; Charters</span></div>
<div class="abs tagline">Training Today &nbsp; Adventures Tomorrow</div>
<div class="abs motto">Learn. Explore. Experience</div>
<div class="btn btn-gold" style="left:916px;top:16px;width:171px;height:42px;font-size:13px">
  <svg width="14" height="16" viewBox="0 0 14 16" fill="none" stroke="#fff" stroke-width="1.6"><circle cx="7" cy="2.5" r="1.6"/><path d="M7 4v11M3 7h8M1 10c1 3 3 4.5 6 5c3-.5 5-2 6-5"/></svg>Book a Charter</div>
<div class="abs navbar"></div>
<div class="nav-link active" style="left:322px">Home</div>
<div class="nav-link" style="left:403px">Boat Training</div>
<div class="nav-link" style="left:529px">Charters</div>
<div class="nav-link" style="left:623px">Plan Ahead Series</div>
<div class="nav-link" style="left:776px">About</div>
<div class="nav-link" style="left:854px">Blog</div>
<div class="nav-link" style="left:922px">Contact</div>
<div class="abs nav-active-bar"></div>
<svg class="abs" style="left:1063px;top:86px" width="18" height="18" viewBox="0 0 18 18" fill="none" stroke="#fff" stroke-width="1.8"><circle cx="7.5" cy="7.5" r="6"/><path d="M12 12l5 5"/></svg>

<!-- Hero -->
<div class="abs hero-media" role="img" aria-label="Couple cruising on a motorboat across calm water at sunset"></div>
<div class="abs hero-shade"></div>
<h1 class="abs display hero-title">CONFIDENCE<br>AT THE HELM</h1>
<div class="abs hero-kicker">TRAINING &#9679; CHARTERS &#9679; REAL-WORLD KNOWLEDGE</div>
<p class="abs hero-copy">Whether you're new to boating or ready for your next adventure, Captain Harlow's Boat Training &amp; Charters, LLC helps you build skills, make memories, and explore with confidence.</p>
<div class="btn btn-navy" style="left:109px;top:540px;width:222px;height:40px;font-size:13.5px">
  <svg width="14" height="16" viewBox="0 0 14 16" fill="none" stroke="#fff" stroke-width="1.6"><circle cx="7" cy="2.5" r="1.6"/><path d="M7 4v11M3 7h8M1 10c1 3 3 4.5 6 5c3-.5 5-2 6-5"/></svg>Explore Our Charters</div>
<div class="btn btn-gold" style="left:344px;top:540px;width:204px;height:40px;font-size:13.5px">
  <svg width="14" height="16" viewBox="0 0 14 16" fill="none" stroke="#fff" stroke-width="1.6"><circle cx="7" cy="2.5" r="1.6"/><path d="M7 4v11M3 7h8M1 10c1 3 3 4.5 6 5c3-.5 5-2 6-5"/></svg>View Boat Training</div>
<div class="abs hero-quote">"A safer, more confident boater makes a brighter tomorrow on the water."<br><span style="font-style:normal;padding-left:12px">— Captain Harlow</span></div>
<div class="dot" style="left:576px"></div>
<div class="dot" style="left:595px;background:var(--gold)"></div>
<div class="dot" style="left:614px"></div>

<!-- Book series -->
<div class="abs books-bg" role="img" aria-label="Soft boat wake spray on light water"></div>
<div class="eyebrow" style="top:772px">KNOWLEDGE FOR A BETTER BOATING TOMORROW</div>
<h2 class="section-title display" style="top:806px;color:var(--navy)">THE PLAN AHEAD <span class="hl">SERIES</span></h2>
<div class="section-sub" style="top:864px">Practical guidance. Real-world insights. A safer, smarter you</div>
<div class="book" style="left:170px;width:228px" role="img" aria-label="Book cover: Plan Your Purchase by Captain Harlow B. Venrick"></div>
<div class="book" style="left:488px;width:240px" role="img" aria-label="Book cover: Plan Your Throttle by Captain Harlow B. Venrick"></div>
<div class="book" style="left:808px;width:234px" role="img" aria-label="Book cover: Plan Your Trip by Captain Harlow B. Venrick"></div>
<div class="btn btn-gold" style="left:416px;top:1336px;width:368px;height:42px;font-size:13.5px">
  <svg width="22" height="22" viewBox="0 0 22 22"><circle cx="11" cy="11" r="10" fill="#fff"/></svg>View the Plan Ahead Series on Bookhaven</div>
<div class="abs books-note">Visit Captain Harlow's Bookhaven Author Page</div>

<!-- Meet the captain -->
<div class="abs captain-photo" role="img" aria-label="Portrait of Captain Harlow in a grey polo shirt"></div>
<div class="abs meet">MEET CAPTAIN HARLOW</div>
<h2 class="abs display cap-head">EXPERIENCE.KNOWLEDGE.<br><span class="hl">A SAFER TOMORROW.</span></h2>
<p class="abs cap-copy">I'm Captain Harlow, a U.S. Coast Guard licensed captain, certified boating instructor, and author of the Plan Ahead series. With years of hands-on experience on the water, I'm passionate about helping others build the skills and confidence to boat safely and enjoyably. Whether you're training, chartering, or just looking for trusted guidance, I'm here to help you make the most of your time on the water</p>
<div class="btn btn-navy" style="left:395px;top:1886px;width:162px;height:42px;font-size:14px;text-transform:uppercase">
  <svg width="14" height="16" viewBox="0 0 14 16" fill="none" stroke="#fff" stroke-width="1.6"><circle cx="7" cy="2.5" r="1.6"/><path d="M7 4v11M3 7h8M1 10c1 3 3 4.5 6 5c3-.5 5-2 6-5"/></svg>More About Me</div>

<div class="cred" style="top:1565px"><i><svg width="18" height="20" viewBox="0 0 14 16" fill="none" stroke="#fff" stroke-width="1.6"><circle cx="7" cy="2.5" r="1.6"/><path d="M7 4v11M3 7h8M1 10c1 3 3 4.5 6 5c3-.5 5-2 6-5"/></svg></i><span>U.S. Coast Guard Licensed Captain<br>(Master, Near Coastal)</span></div>
<div class="cred" style="top:1628px"><i class="g"><svg width="16" height="18" viewBox="0 0 16 18" fill="#fff"><path d="M8 1l7 3v5c0 4-3 7-7 8c-4-1-7-4-7-8V4z"/></svg></i><span>Certified Boating Instructor</span></div>
<div class="cred" style="top:1682px"><i><svg width="18" height="14" viewBox="0 0 18 14" fill="none" stroke="#fff" stroke-width="1.6"><path d="M1 2c3-1 6-1 8 1c2-2 5-2 8-1v11c-3-1-6-1-8 1c-2-2-5-2-8-1zM9 3v11"/></svg></i><span>Published Author - The Plan Ahead Series</span></div>
<div class="cred" style="top:1736px"><i><svg width="22" height="22" viewBox="0 0 22 22" fill="none" stroke="#fff" stroke-width="1.6"><circle cx="11" cy="11" r="6"/><circle cx="11" cy="11" r="2"/><path d="M11 1v20M1 11h20M4 4l14 14M18 4L4 18"/></svg></i><span>Years of Real-World Charter Experience</span></div>
<div class="cred" style="top:1790px"><i><svg width="22" height="16" viewBox="0 0 22 16" fill="#fff"><circle cx="11" cy="4" r="3"/><circle cx="4" cy="6" r="2.4"/><circle cx="18" cy="6" r="2.4"/><path d="M5 16c0-4 3-6 6-6s6 2 6 6zM0 15c0-3 2-5 4-5c1 0 2 .5 2 1c-1 1-2 2-2 4zM22 15c0-3-2-5-4-5c-1 0-2 .5-2 1c1 1 2 2 2 4z"/></svg></i><span>Committed to Safer, More Confident Boaters</span></div>
<div class="abs cap-quote">"Good Boaters Make Brighter Tomorrows."<br><span>--Captain Harlow</span></div>

<!-- Testimonials -->
<div class="abs reviews-bg" role="img" aria-label="Aerial view of a boat cutting through deep blue water"></div>
<div class="eyebrow" style="top:2086px;color:var(--white)">REAL BOATERS. REAL EXPERIENCES.</div>
<h2 class="section-title display" style="top:2118px;color:var(--white)">CLIENT <span class="hl">TESTIMONIALS</span></h2>
<div class="section-sub" style="top:2176px;color:var(--white);font-weight:500">See what our students and charter guests are saying.</div>

<div class="arrow-c" style="left:26px"><svg width="10" height="12" viewBox="0 0 10 12" fill="none" stroke="#fff" stroke-width="2"><path d="M7 1L2 6l5 5"/></svg></div>
<div class="arrow-c" style="left:1148px"><svg width="10" height="12" viewBox="0 0 10 12" fill="none" stroke="#fff" stroke-width="2"><path d="M3 1l5 5l-5 5"/></svg></div>

<div class="card rating-card" style="left:86px;width:250px">
  <div style="position:absolute;left:34px;top:24px;font-size:34px;font-weight:500;color:var(--navy)">ReviewSpot</div>
  <div class="stars" style="left:36px;top:72px;font-size:22px">★★★★★</div>
  <div style="position:absolute;left:36px;top:110px;font-size:22px;color:var(--ink)"><b style="font-size:36px">4.9</b> &nbsp;out of 5</div>
  <div style="position:absolute;left:36px;top:164px;font-size:17px">Based on 87 reviews</div>
</div>
<div class="card" style="left:354px;width:250px">
  <div class="avatar" role="img" aria-label="Reviewer photo"></div>
  <div class="rv-name">Jennifer R.</div><div class="qmark">&#8221;</div>
  <div class="stars" style="left:108px;top:58px">★★★★★</div>
  <p class="rv-text">"Captain Harlow is an outstanding instructor! Patient, knowledgeable, and made learning to boat fun and stress-free."</p>
</div>
<div class="card" style="left:616px;width:249px">
  <div class="avatar" role="img" aria-label="Reviewer photo"></div>
  <div class="rv-name">Mark T.</div><div class="qmark">&#8221;</div>
  <div class="stars" style="left:108px;top:58px">★★★★★</div>
  <p class="rv-text">"Our charter was the highlight of our vacation. Professional, safe, and an incredible experience on the water!"</p>
</div>
<div class="card" style="left:881px;width:250px">
  <div class="avatar" role="img" aria-label="Reviewer photo"></div>
  <div class="rv-name">David L.</div><div class="qmark">&#8221;</div>
  <div class="stars" style="left:108px;top:58px">★★★★★</div>
  <p class="rv-text">"The Plan Ahead series is a must-read for any boater. Practical, clear, and filled with real-world tips."</p>
</div>

<!-- Services -->
<div class="eyebrow" style="top:2641px">ON THE WATER AND BEYOND</div>
<h2 class="section-title display" style="top:2674px;color:var(--navy)">OUR <span class="hl">SERVICES</span></h2>
<div class="section-sub" style="top:2724px">Training, Captaining &amp; Deliveries</div>

<div class="svc" style="left:114px">
  <div class="ic"><svg width="34" height="26" viewBox="0 0 34 26" fill="var(--navy)"><circle cx="17" cy="5" r="4"/><path d="M11 10h12l-2 8H13zM2 18h30l-4 6H6z"/></svg></div>
  <h3>Boat Training</h3><p>Hands-on instruction for new<br>and experienced boaters</p><a>LEARN MORE &gt;</a>
</div>
<div class="svc" style="left:358px">
  <div class="ic"><svg width="36" height="24" viewBox="0 0 36 24" fill="var(--navy)"><path d="M12 4h12l4 7H8zM2 13h32l-5 8H7z"/></svg></div>
  <h3>Charters</h3><p>Relax and explore with<br>captain-guided charters</p><a>VIEW CHARTERS &gt;</a>
</div>
<div class="svc feat" style="left:608px">
  <div class="ic"><svg width="32" height="24" viewBox="0 0 18 14" fill="none" stroke="var(--gold)" stroke-width="1.4"><path d="M1 2c3-1 6-1 8 1c2-2 5-2 8-1v11c-3-1-6-1-8 1c-2-2-5-2-8-1zM9 3v11"/></svg></div>
  <h3>Plan Ahead Series</h3><p>Books to help you make<br>informed decisions on and off<br>the water.</p><a>SEE THE BOOKS &gt;</a>
</div>
<div class="svc" style="left:856px">
  <div class="ic"><svg width="32" height="26" viewBox="0 0 32 26" fill="var(--navy)"><circle cx="8" cy="6" r="3.5"/><circle cx="16" cy="5" r="3.5"/><circle cx="24" cy="6" r="3.5"/><path d="M2 14h28v4H2zM4 20h24v4H4z"/></svg></div>
  <h3>Private Coaching</h3><p>Personalized training for<br>your goals.</p><a>GET STARTED &gt;</a>
</div>

<!-- Footer -->
<svg class="abs" style="left:0;top:3070px" width="1200" height="299" viewBox="0 0 1200 299" preserveAspectRatio="none">
  <path d="M0 40C120 10 240 10 360 40S600 90 700 40S950-5 1100 30C1150 40 1180 45 1200 40V299H0z" fill="var(--navy)"/>
</svg>
<div class="abs footer-motto">Good Boats. Great People.<br>Brighter Tomorrows.</div>
<div class="abs footer-badge">Captain Harlow's Boat Training &amp; Charters</div>
<div class="btn btn-gold" style="left:952px;top:3190px;width:138px;height:40px;font-size:13px">
  <svg width="14" height="16" viewBox="0 0 14 16" fill="none" stroke="#fff" stroke-width="1.6"><circle cx="7" cy="2.5" r="1.6"/><path d="M7 4v11M3 7h8M1 10c1 3 3 4.5 6 5c3-.5 5-2 6-5"/></svg>Contact Us</div>
<div class="abs footer-line">Training. Charters. Books. A Safer Tomorrow.</div>
<div class="abs rule"></div>
<div class="abs copy">© 2026 Captain Harlow's Boat Training &amp; Charters, LLC. All rights reserved.</div>
<div class="social" style="left:916px"></div>
<div class="social" style="left:951px"></div>
<div class="social" style="left:987px"></div>
<div class="social" style="left:1025px"></div>
<div class="social" style="left:1063px"></div>

</body>
</html>
```